Business Card Design

We are an IT staffing and consulting company providing IT solutions and resources to our clients.

Industry/Entity Type

Business

Contact Information for Business Card

Ramesh Tulavarthi
Vice President

BrightNode Inc
48215 Harrowmere Court Square, suite 700
Ashburn, VA 20147
Direct: 571-555-0193
Mobile: 571-555-0147
Email: Ramesh@brightnodeinc.com
Fax: 703-555-0162
www.brightnodeinc.com

```html
<!DOCTYPE html>
<html lang="en">
<head>
<meta charset="utf-8">
<title>BrightNode Business Card</title>
<link href="https://fonts.googleapis.com/css2?family=Open+Sans:wght@400;600;700&display=swap" rel="stylesheet">
<style>
  :root {
    --bg: #e4e4e4;
    --card: #fbfbfb;
    --red: #be1a2e;
    --black: #080808;
    --ink: #3a3a3a;
    --white: #ffffff;
  }
  * { margin: 0; padding: 0; box-sizing: border-box; }
  html, body { width: 1200px; height: 883px; overflow: hidden; }
  body {
    background: var(--bg);
    font-family: "Open Sans", Arial, sans-serif;
    position: relative;
  }
  .card {
    position: absolute;
    width: 540px;
    height: 310px;
    background: var(--card);
    border-radius: 30px;
    overflow: hidden;
    box-shadow: 0 10px 24px rgba(0,0,0,0.12);
  }
  .card-back { left: 580px; top: 110px; }
  .card-front { left: 110px; top: 460px; }
  .card-shapes { position: absolute; inset: 0; }

  /* back */
  .brand {
    position: absolute;
    left: 52px; top: 128px;
    display: flex; align-items: center; gap: 12px;
  }
  .brand-dot { width: 22px; height: 22px; border-radius: 50%; background: var(--red); }
  .brand-name { font-size: 40px; font-weight: 400; color: var(--ink); letter-spacing: 0.5px; }
  .back-url {
    position: absolute;
    left: 295px; top: 45px; width: 175px; height: 60px;
    display: flex; align-items: center; justify-content: center;
    color: var(--white); font-size: 8.5px; letter-spacing: 1.2px;
    text-transform: uppercase; white-space: nowrap;
  }

  /* front */
  .holder {
    position: absolute; left: 130px; top: 26px; width: 300px;
    text-align: center; color: var(--ink); text-transform: uppercase;
  }
  .holder-name { font-size: 22px; font-weight: 400; line-height: 1.1; }
  .holder-name b { font-weight: 700; }
  .holder-title { font-size: 11px; line-height: 1.4; }
  .holder-title b { font-weight: 700; }
  .contact-block {
    position: absolute; color: var(--white);
    text-transform: uppercase; line-height: 1.3; white-space: nowrap;
  }
  .phone { left: 40px; top: 154px; font-size: 13.5px; }
  .web { left: 292px; top: 96px; width: 240px; text-align: center; font-size: 12.5px; }
  .address {
    position: absolute; left: 215px; top: 254px; width: 315px;
    text-align: center; color: var(--ink); font-size: 10.5px; line-height: 1.4;
    text-transform: uppercase; white-space: nowrap;
  }
  .address b { font-weight: 700; }
</style>
</head>
<body>

  <section class="card card-back" aria-label="Business card back">
    <svg class="card-shapes" width="540" height="310" viewBox="0 0 540 310">
      <rect x="295" y="45" width="175" height="60" fill="var(--black)"/>
      <rect x="470" y="45" width="70" height="60" fill="var(--red)"/>
    </svg>
    <div class="brand">
      <span class="brand-dot"></span>
      <span class="brand-name">BrightNode</span>
    </div>
    <div class="back-url">www.brightnodeinc.com</div>
  </section>

  <section class="card card-front" aria-label="Business card front">
    <svg class="card-shapes" width="540" height="310" viewBox="0 0 540 310">
      <polygon points="0,145 275,145 300,245 0,245" fill="var(--red)"/>
      <polygon points="258,80 540,80 540,185 285,185" fill="var(--black)"/>
      <rect x="0" y="160" width="12" height="85" fill="var(--black)"/>
    </svg>
    <div class="holder">
      <p class="holder-name">Ramesh <b>Tulavarthi</b></p>
      <p class="holder-title"><b>Vice</b> President</p>
    </div>
    <div class="contact-block phone">
      <p>Direct: 571-555-0193</p>
      <p>Mobile: 571-555-0147</p>
      <p>Fax: 703-555-0162</p>
    </div>
    <div class="contact-block web">
      <p>Email &amp; Web</p>
      <p>Ramesh@brightnodeinc.com</p>
      <p>www.brightnodeinc.com</p>
    </div>
    <div class="address">
      <p>48215 <b>Harrowmere</b> Court Square, <b>Suite 700</b></p>
      <p><b>Ashburn, VA 20147</b></p>
    </div>
  </section>

</body>
</html>
```